Re-drawing and gpahically, according to coorporate design

Three flowcharts need to be re-drawn and graphically improved according to coorporate design

```html
<!DOCTYPE html>
<html lang="en">
<head>
<meta charset="utf-8">
<title>Carbon &amp; Energy Value Chain</title>
<link rel="stylesheet" href="https://fonts.googleapis.com/css2?family=Barlow+Condensed:wght@400;500;600&display=swap">
<style>
  :root {
    --olive: #9ca61d;
    --teal: #4a6766;
    --slate: #707176;
    --flow-olive: #e5e7c7;
    --flow-grey: #dcdde0;
    --sun-core: #f6a935;
    --sun-ray: #e0a552;
    --ink-logo: #55575c;
    --white: #ffffff;
  }
  html, body { margin: 0; padding: 0; overflow: hidden; background: var(--white); }
  .canvas { width: 1040px; height: 1200px; display: block; }
  svg text { font-family: "Barlow Condensed", sans-serif; }
  .label { fill: var(--white); font-size: 30px; font-weight: 400; text-anchor: middle; }
  .label-lg { fill: var(--white); font-size: 56px; font-weight: 400; text-anchor: middle; }
  .label-sun { fill: var(--white); font-size: 66px; font-weight: 400; text-anchor: middle; }
  .caption { fill: var(--slate); font-size: 24px; font-weight: 600; text-anchor: middle; }
  .partner { fill: var(--ink-logo); font-size: 26px; font-weight: 500; }
  .flow-olive { fill: var(--flow-olive); }
  .flow-grey { fill: var(--flow-grey); }
  .node-olive { fill: var(--olive); }
  .node-teal { fill: var(--teal); }
  .node-slate { fill: var(--slate); }
  .atom { fill: var(--olive); }
  .atom-h { fill: var(--white); }
  .atom-txt { fill: var(--white); font-size: 30px; text-anchor: middle; }
  .atom-h-txt { fill: var(--slate); font-size: 24px; text-anchor: middle; }
  .bond { stroke: var(--white); stroke-width: 5; }
  .icon { fill: var(--white); }
  .icon-line { fill: none; stroke: var(--white); stroke-width: 6; }
</style>
</head>
<body>
<svg class="canvas" viewBox="0 0 1780 2070" preserveAspectRatio="xMidYMid meet" role="img" aria-label="Value chain from sun and renewable electricity through residues and CO2 to products">

  <g class="flows">
    <polygon class="flow-grey" points="378,220 535,198 535,242"/>
    <polygon class="flow-grey" points="745,220 885,200 885,240"/>
    <polygon class="flow-olive" points="1100,215 1430,150 1430,228"/>
    <polygon class="flow-olive" points="1100,228 1430,300 1410,365"/>
    <polygon class="flow-grey" points="668,318 885,445 872,492"/>
    <polygon class="flow-grey" points="985,318 945,420 975,420"/>
    <polygon class="flow-olive" points="918,562 705,702 780,702"/>
    <polygon class="flow-olive" points="938,562 905,702 970,702"/>
    <polygon class="flow-olive" points="965,562 1090,702 1175,702"/>
    <polygon class="flow-olive" points="740,820 848,950 848,1030"/>
    <polygon class="flow-olive" points="940,820 925,896 958,896"/>
    <polygon class="flow-olive" points="1140,820 1034,950 1034,1030"/>
    <polygon class="flow-grey" points="1222,730 1426,500 1426,620"/>
    <polygon class="flow-grey" points="1222,748 1426,700 1426,800"/>
    <polygon class="flow-grey" points="1222,778 1426,920 1426,1005"/>
    <polygon class="flow-grey" points="569,745 660,762 569,780"/>
    <polygon class="flow-grey" points="196,380 182,481 212,481"/>
    <polygon class="flow-grey" points="196,735 180,861 212,861"/>
    <polygon class="flow-grey" points="196,1070 180,1190 212,1190"/>
    <polygon class="flow-grey" points="196,1365 180,1494 212,1494"/>
    <polygon class="flow-grey" points="298,1220 460,1334 575,1334"/>
    <polygon class="flow-grey" points="905,1108 705,1334 845,1334"/>
    <polygon class="flow-grey" points="924,1108 930,1334 1060,1334"/>
    <polygon class="flow-grey" points="940,1108 1160,1334 1290,1334"/>
    <polygon class="flow-grey" points="958,1108 1300,1334 1535,1334"/>
    <polygon class="flow-olive" points="550,1460 537,1590 563,1590"/>
    <polygon class="flow-olive" points="770,1460 757,1590 783,1590"/>
    <polygon class="flow-olive" points="1000,1460 987,1590 1013,1590"/>
    <polygon class="flow-olive" points="1230,1460 1217,1590 1243,1590"/>
    <polygon class="flow-olive" points="1494,1460 1481,1590 1507,1590"/>
  </g>

  <g class="sun" transform="translate(197,208)">
    <g fill="var(--sun-ray)">
      <polygon points="-6,-95 6,-95 0,-155"/>
      <polygon points="-6,95 6,95 0,155"/>
      <polygon points="-95,-6 -95,6 -155,0"/>
      <polygon points="95,-6 95,6 155,0"/>
      <polygon points="-6,-95 6,-95 0,-155" transform="rotate(30)"/>
      <polygon points="-6,-95 6,-95 0,-155" transform="rotate(60)"/>
      <polygon points="-6,-95 6,-95 0,-155" transform="rotate(120)"/>
      <polygon points="-6,-95 6,-95 0,-155" transform="rotate(150)"/>
      <polygon points="-6,-95 6,-95 0,-155" transform="rotate(210)"/>
      <polygon points="-6,-95 6,-95 0,-155" transform="rotate(240)"/>
      <polygon points="-6,-95 6,-95 0,-155" transform="rotate(300)"/>
      <polygon points="-6,-95 6,-95 0,-155" transform="rotate(330)"/>
      <polygon points="-4,-92 4,-92 0,-125" transform="rotate(15)"/>
      <polygon points="-4,-92 4,-92 0,-125" transform="rotate(45)"/>
      <polygon points="-4,-92 4,-92 0,-125" transform="rotate(75)"/>
      <polygon points="-4,-92 4,-92 0,-125" transform="rotate(105)"/>
      <polygon points="-4,-92 4,-92 0,-125" transform="rotate(135)"/>
      <polygon points="-4,-92 4,-92 0,-125" transform="rotate(165)"/>
      <polygon points="-4,-92 4,-92 0,-125" transform="rotate(195)"/>
      <polygon points="-4,-92 4,-92 0,-125" transform="rotate(225)"/>
      <polygon points="-4,-92 4,-92 0,-125" transform="rotate(255)"/>
      <polygon points="-4,-92 4,-92 0,-125" transform="rotate(285)"/>
      <polygon points="-4,-92 4,-92 0,-125" transform="rotate(315)"/>
      <polygon points="-4,-92 4,-92 0,-125" transform="rotate(345)"/>
    </g>
    <circle r="80" fill="var(--sun-core)"/>
    <text class="label-sun" y="22">Sun</text>
  </g>

  <g class="node agriculture">
    <rect class="node-slate" x="535" y="127" width="205" height="185" rx="10"/>
    <g class="icon">
      <rect x="634" y="145" width="6" height="85"/>
      <ellipse cx="637" cy="155" rx="6" ry="12"/>
      <ellipse cx="628" cy="178" rx="7" ry="12"/><ellipse cx="646" cy="178" rx="7" ry="12"/>
      <ellipse cx="628" cy="200" rx="7" ry="12"/><ellipse cx="646" cy="200" rx="7" ry="12"/>
      <ellipse cx="628" cy="220" rx="7" ry="11"/><ellipse cx="646" cy="220" rx="7" ry="11"/>
    </g>
    <text class="label" x="640" y="270">AGRICULTURE/</text>
    <text class="label" x="640" y="300">FORESTRY</text>
  </g>
  <g class="node industry">
    <rect class="node-slate" x="885" y="127" width="205" height="185" rx="10"/>
    <g class="icon">
      <circle cx="972" cy="160" r="12"/><circle cx="990" cy="155" r="14"/><circle cx="1004" cy="162" r="10"/>
      <rect x="945" y="175" width="16" height="75"/>
      <polygon points="961,250 961,210 990,195 990,210 1012,195 1012,210 1036,195 1036,250"/>
      <rect x="936" y="248" width="102" height="6"/>
    </g>
    <text class="label" x="987" y="296">INDUSTRY</text>
  </g>

  <g class="node food">
    <circle class="node-olive" cx="1492" cy="175" r="78"/>
    <text class="label" x="1492" y="186">Food/feed</text>
  </g>
  <g class="node wood">
    <circle class="node-olive" cx="1492" cy="350" r="78"/>
    <text class="label" x="1492" y="358">Wood Based</text>
    <text class="label" x="1492" y="386">Products</text>
  </g>

  <g class="node residues">
    <circle class="node-olive" cx="940" cy="482" r="68"/>
    <text class="label" x="940" y="492">RESIDUES</text>
  </g>

  <g class="node electricity">
    <rect class="node-teal" x="108" y="481" width="182" height="252" rx="10"/>
    <path class="icon-line" d="M150,630 A75,75 0 0 1 175,510"/>
    <path class="icon-line" d="M240,505 A75,75 0 0 1 215,640"/>
    <polygon class="icon" points="212,500 165,585 195,585 178,650 230,555 200,555"/>
    <text class="label" x="199" y="690">RENEWABLE</text>
    <text class="label" x="199" y="720">ELECTRICITY</text>
  </g>
  <g class="node electrolysis">
    <rect class="node-teal" x="108" y="861" width="182" height="208" rx="10"/>
    <g class="icon">
      <circle cx="197" cy="888" r="14"/>
      <rect x="160" y="885" width="75" height="12"/>
      <rect x="150" y="905" width="40" height="82"/>
      <rect x="202" y="905" width="45" height="82"/>
      <rect x="150" y="992" width="40" height="22"/>
      <rect x="202" y="992" width="45" height="22"/>
    </g>
    <g stroke="var(--teal)" stroke-width="4">
      <line x1="205" y1="920" x2="247" y2="920"/><line x1="205" y1="935" x2="247" y2="935"/>
      <line x1="205" y1="950" x2="247" y2="950"/><line x1="205" y1="965" x2="247" y2="965"/>
      <line x1="158" y1="1002" x2="172" y2="1002"/><line x1="165" y1="995" x2="165" y2="1009"/>
      <line x1="220" y1="1002" x2="236" y2="1002"/>
    </g>
    <text class="label" x="199" y="1058">ELECTROLYSIS</text>
  </g>
  <g class="node hydrogen">
    <rect class="node-teal" x="108" y="1190" width="182" height="170" rx="10"/>
    <line class="bond" x1="163" y1="1272" x2="233" y2="1228"/>
    <circle class="atom" cx="233" cy="1228" r="30"/>
    <circle class="atom" cx="163" cy="1272" r="30"/>
    <text class="atom-txt" x="233" y="1239">H</text>
    <text class="atom-txt" x="163" y="1283">H</text>
    <text class="label" x="199" y="1348">HYDROGEN</text>
  </g>
  <g class="node direct">
    <rect class="node-slate" x="123" y="1494" width="148" height="233" rx="10"/>
    <text class="label" x="197" y="1532">Various</text>
    <text class="label" x="197" y="1567">Direct</text>
    <text class="label" x="197" y="1602">Applications</text>
    <text class="label" x="197" y="1637">-Mobility</text>
    <text class="label" x="197" y="1672">-Industry</text>
    <text class="label" x="197" y="1707">-Gas Grid</text>
  </g>

  <text class="caption" x="477" y="648">GREENING THE GAS</text>
  <g class="node methane">
    <rect class="node-teal" x="386" y="656" width="183" height="207" rx="10"/>
    <g class="bond">
      <line x1="474" y1="755" x2="425" y2="703"/><line x1="474" y1="755" x2="509" y2="689"/>
      <line x1="474" y1="755" x2="428" y2="803"/><line x1="474" y1="755" x2="536" y2="783"/>
    </g>
    <circle class="atom-h" cx="425" cy="703" r="18"/><circle class="atom-h" cx="509" cy="689" r="21"/>
    <circle class="atom-h" cx="428" cy="803" r="18"/><circle class="atom-h" cx="536" cy="783" r="18"/>
    <text class="atom-h-txt" x="425" y="712">H</text><text class="atom-h-txt" x="509" y="698">H</text>
    <text class="atom-h-txt" x="428" y="812">H</text><text class="atom-h-txt" x="536" y="792">H</text>
    <circle class="atom" cx="474" cy="755" r="34"/>
    <text class="atom-txt" x="474" y="766">C</text>
    <text class="label" x="477" y="850">CH4</text>
  </g>

  <g class="node process">
    <rect class="node-olive" x="665" y="702" width="152" height="113" rx="8"/>
    <text class="label" x="741" y="754">Anaerobic</text>
    <text class="label" x="741" y="786">Digestion</text>
  </g>
  <g class="node process">
    <rect class="node-olive" x="863" y="702" width="152" height="113" rx="8"/>
    <text class="label" x="939" y="754">Biomass</text>
    <text class="label" x="939" y="786">Gasification</text>
  </g>
  <g class="node process">
    <rect class="node-olive" x="1062" y="702" width="152" height="113" rx="8"/>
    <text class="label" x="1138" y="770">Fermentation</text>
  </g>

  <g class="node co2">
    <rect class="node-teal" x="846" y="896" width="190" height="199" rx="10"/>
    <g class="bond">
      <line x1="939" y1="1002" x2="885" y2="935"/><line x1="939" y1="1002" x2="986" y2="941"/>
    </g>
    <circle class="atom-h" cx="885" cy="935" r="18"/><circle class="atom-h" cx="986" cy="941" r="18"/>
    <text class="atom-h-txt" x="885" y="944">O</text><text class="atom-h-txt" x="986" y="950">O</text>
    <circle class="atom" cx="939" cy="1002" r="34"/>
    <text class="atom-txt" x="939" y="1013">C</text>
    <text class="label" x="941" y="1080">CO2</text>
  </g>

  <g class="node polymers">
    <rect class="node-slate" x="1426" y="479" width="165" height="148" rx="10"/>
    <g class="icon-line" stroke-width="4">
      <polygon points="1487,493 1505,503 1505,524 1487,534 1469,524 1469,503"/>
      <polygon points="1523,513 1541,523 1541,544 1523,554 1505,544 1505,523"/>
      <polygon points="1487,534 1505,544 1505,565 1487,575 1469,565 1469,544"/>
    </g>
    <text class="label" x="1508" y="618">POLYMERS</text>
  </g>
  <g class="node chemicals">
    <rect class="node-slate" x="1426" y="679" width="165" height="148" rx="10"/>
    <rect class="icon" x="1494" y="697" width="30" height="5"/>
    <path class="icon" d="M1500,702 h18 v30 l26,44 h-70 l26,-44 z"/>
    <circle cx="1505" cy="745" r="6" fill="var(--slate)"/>
    <circle cx="1518" cy="760" r="7" fill="var(--slate)"/>
    <circle cx="1497" cy="762" r="4" fill="var(--slate)"/>
    <text class="label" x="1508" y="818">CHEMICALS</text>
  </g>
  <g class="node fuels">
    <rect class="node-slate" x="1426" y="879" width="165" height="148" rx="10"/>
    <path class="icon" d="M1508,898 C1520,925 1533,945 1533,958 A25,25 0 0 1 1483,958 C1483,945 1496,925 1508,898 z"/>
    <text class="label" x="1508" y="1018">FUELS</text>
  </g>

  <g class="partners-right">
    <rect x="1614" y="538" width="20" height="20" fill="var(--olive)"/>
    <text class="partner" x="1640" y="557">Kestrel Works</text>
    <text class="partner" x="1620" y="760">Ardenway</text>
    <text class="partner" x="1620" y="808">Morrow Union</text>
    <text class="partner" x="1620" y="940">Talvora</text>
    <text class="partner" x="1620" y="1000">Brennick</text>
  </g>

  <g class="node route">
    <rect class="node-slate" x="456" y="1334" width="176" height="122" rx="6"/>
    <text class="label" x="545" y="1374">Catalytic/</text>
    <text class="label" x="545" y="1406">Biological</text>
    <text class="label" x="545" y="1438">Methanation</text>
  </g>
  <g class="node route">
    <rect class="node-slate" x="679" y="1334" width="182" height="122" rx="6"/>
    <text class="label" x="770" y="1374">Electro-</text>
    <text class="label" x="770" y="1406">Chemical</text>
    <text class="label" x="770" y="1438">Conversion</text>
  </g>
  <g class="node route">
    <rect class="node-slate" x="909" y="1334" width="182" height="122" rx="6"/>
    <text class="label" x="1000" y="1374">Other</text>
    <text class="label" x="1000" y="1406">Chemical</text>
    <text class="label" x="1000" y="1438">Transformations</text>
  </g>
  <g class="node route">
    <rect class="node-slate" x="1141" y="1334" width="176" height="122" rx="6"/>
    <text class="label" x="1229" y="1374">Existing</text>
    <text class="label" x="1229" y="1406">Industrial</text>
    <text class="label" x="1229" y="1438">Applications</text>
  </g>
  <g class="node route">
    <rect class="node-olive" x="1405" y="1334" width="175" height="122" rx="6"/>
    <text class="label-lg" x="1492" y="1418">ALGEA</text>
  </g>

  <g class="node product">
    <circle class="node-olive" cx="550" cy="1663" r="78"/>
    <text class="label" x="550" y="1674">CH4</text>
  </g>
  <g class="node product">
    <circle class="node-olive" cx="768" cy="1663" r="78"/>
    <text class="label" x="768" y="1674">Ethyleneoxide</text>
    <text class="label" x="768" y="1705">C2H4O</text>
  </g>
  <g class="node product">
    <circle class="node-olive" cx="998" cy="1663" r="78"/>
    <text class="label" x="998" y="1664">Polyols,</text>
    <text class="label" x="998" y="1695">Polymers</text>
  </g>
  <g class="node product">
    <circle class="node-olive" cx="1228" cy="1663" r="78"/>
    <text class="label" x="1228" y="1664">Beverage</text>
    <text class="label" x="1228" y="1695">Industry</text>
  </g>
  <g class="node product">
    <circle class="node-olive" cx="1492" cy="1663" r="78"/>
    <text class="label" x="1492" y="1664">Fuel, Bio-</text>
    <text class="label" x="1492" y="1695">Polymers</text>
  </g>

  <g class="partners-bottom">
    <circle cx="1258" cy="1520" r="10" fill="var(--olive)"/>
    <text class="partner" x="1276" y="1528">Quillon</text>
    <text class="partner" x="462" y="1792">Peregrine Hall</text>
    <text class="partner" x="462" y="1856">Osmund</text>
    <circle cx="470" cy="1922" r="14" fill="var(--olive)"/>
    <text class="partner" x="494" y="1932">Quillon</text>
    <text class="partner" x="462" y="1990">Harlow Tessel</text>
    <text class="partner" x="700" y="1794">Vantrel</text>
  </g>
</svg>
</body>
</html>
```